A Speech Therapy Business needs to update their logo

I need an update to the font and color of my logo to look more appealing. I am looking to open a private practice as a Speech Language Pathologist that caters to adults and children. It needs to be sophisticated and friendly at the same time. I want to keep the silhouette in my logo as is, just update the font and color for "Brightpath".
Industry/Entity Type
Business
Contact Information for Business Card
I want the business card to have my logo, my name (Odile Varn, CCC-SLP, TSSLD) and that I am a Bilingual Speech Language Pathologist. Also, include my phone number, (718) 555-0193. Include my website, Brightpathslp.example, and email address, odilevarn@brightpathslp.example
Look and feel

```html
<!DOCTYPE html>
<html lang="en">
<head>
<meta charset="utf-8">
<title>Brightpath Business Card</title>
<link rel="stylesheet" href="https://fonts.googleapis.com/css2?family=Arimo:wght@400;700&display=swap">
<style>
  :root {
    --backdrop: #ecebee;
    --card: #ffffff;
    --blue: #2160c4;
    --sky: #4fb3df;
    --violet: #7a4bb5;
    --magenta: #c04aa6;
    --silhouette: #2a2a30;
    --ink: #1d1d22;
    --muted: #4a4a52;
  }
  * { box-sizing: border-box; margin: 0; padding: 0; }
  html, body {
    width: 1200px; height: 800px; overflow: hidden;
    background: var(--backdrop);
    font-family: "Arimo", Arial, sans-serif;
  }
  .card {
    position: absolute; left: 110px; top: 120px;
    width: 980px; height: 560px;
    background: var(--card);
    box-shadow: 0 10px 30px rgba(0,0,0,.12);
    overflow: hidden;
  }
  .puzzle-field { position: absolute; left: 0; top: 0; width: 980px; height: 560px; }
  .logo-block {
    position: absolute; right: 60px; top: 36px;
    display: flex; flex-direction: column; align-items: flex-end; gap: 10px;
  }
  .silhouette-art {
    width: 440px; height: 78px;
    margin-right: 30px;
    background: linear-gradient(90deg, #2a2a30 0%, #3a3a42 60%, #55555e 100%);
    border-radius: 6px;
    opacity: .85;
  }
  .brand { display: flex; align-items: center; gap: 14px; }
  .brand-dot { width: 28px; height: 28px; border-radius: 50%; background: var(--violet); flex: none; }
  .brand-name {
    font-size: 68px; font-weight: 700; color: var(--violet);
    letter-spacing: 1px; text-transform: uppercase; line-height: 1;
    white-space: nowrap;
  }
  .contact { position: absolute; left: 580px; top: 280px; }
  .contact-name { color: var(--blue); font-size: 30px; font-weight: 400; white-space: nowrap; }
  .contact-name .credentials { font-size: 19px; }
  .contact-role { color: var(--muted); font-size: 16px; margin: 4px 0 16px 18px; }
  .contact-list { list-style: none; }
  .contact-item {
    display: flex; align-items: center; gap: 8px;
    color: var(--ink); font-size: 20px; line-height: 1.5;
    white-space: nowrap;
  }
  .contact-item svg { width: 20px; height: 20px; flex: none; }
</style>
</head>
<body>
  <main class="card">
    <svg class="puzzle-field" viewBox="0 0 980 560" role="img" aria-label="Scattered jigsaw puzzle pieces fading from sky blue through violet to magenta">
      <defs>
        <linearGradient id="puzzleTone" x1="0" y1="0" x2="1" y2="1">
          <stop offset="0" stop-color="#4fb3df"/>
          <stop offset="0.45" stop-color="#2f6cc4"/>
          <stop offset="0.75" stop-color="#7a4bb5"/>
          <stop offset="1" stop-color="#c04aa6"/>
        </linearGradient>
      </defs>
      <path d="M0 170 C80 140 180 130 260 160 C330 190 360 250 400 300 C470 330 540 380 570 450 C590 500 585 540 560 560 H0 Z" fill="url(#puzzleTone)" opacity="0.9"/>
      <rect x="320" y="70" width="24" height="24" fill="#4fb3df" opacity="0.8"/>
      <rect x="250" y="115" width="18" height="18" fill="#3a7cc8" opacity="0.8"/>
      <rect x="460" y="245" width="26" height="26" fill="#6a4ab6" opacity="0.85"/>
      <rect x="515" y="350" width="22" height="22" fill="#8a4ab2" opacity="0.85"/>
    </svg>

    <div class="logo-block">
      <div class="silhouette-art" role="img" aria-label="Silhouette of a family of adults and children walking hand in hand"></div>
      <div class="brand">
        <span class="brand-dot"></span>
        <span class="brand-name">Brightpath</span>
      </div>
    </div>

    <section class="contact">
      <h1 class="contact-name">Odile Varn<span class="credentials">, CCC-SLP, TSSLD</span></h1>
      <p class="contact-role">Bilingual Speech Language Pathologist</p>
      <ul class="contact-list">
        <li class="contact-item">
          <svg viewBox="0 0 24 24" aria-hidden="true"><path fill="#2160c4" d="M6.6 10.8a15 15 0 0 0 6.6 6.6l2.2-2.2a1 1 0 0 1 1-.25 11.4 11.4 0 0 0 3.6.57 1 1 0 0 1 1 1V20a1 1 0 0 1-1 1A17 17 0 0 1 3 4a1 1 0 0 1 1-1h3.5a1 1 0 0 1 1 1c0 1.25.2 2.45.57 3.57a1 1 0 0 1-.25 1z"/></svg>
          (718) 555-0193.
        </li>
        <li class="contact-item">
          <svg viewBox="0 0 24 24" aria-hidden="true"><rect x="2" y="5" width="20" height="14" rx="2" fill="#2160c4"/><path d="M3 6l9 7 9-7" fill="none" stroke="#fff" stroke-width="1.8"/></svg>
          odilevarn@brightpathslp.example
        </li>
        <li class="contact-item">
          <svg viewBox="0 0 24 24" aria-hidden="true"><circle cx="12" cy="12" r="10" fill="#7a4bb5"/><g fill="none" stroke="#fff" stroke-width="1.3"><ellipse cx="12" cy="12" rx="4.5" ry="10"/><path d="M2 12h20M4 7h16M4 17h16"/></g></svg>
          Brightpathslp.example
        </li>
      </ul>
    </section>
  </main>
</body>
</html>
```